Velvet Arc Car Detailing Brochure

I would like a trifold brochure designed for my car detailing business. The background has to be full black or mostly black with some designing using only colors present in our logo.

Front page must have our logo and name, list of services, a photo and mybe our phone number but no long text.

Inside I want to present each service one by one with its description and a photo representing/showing each service. (I will provide the text below). For photos, use stock photos and I will add come of mines already too.

On the back of the brochure I want to have contact & info: phone number, opening hours, address, website, Instagram.

Outside left I want the text About us and photo/design.

I want the brochure to be neat, professional, easy to read, but at the same time not too boring.

Text:
1. About us
a. the ultimate destination for car care in Geneva. We provide personalized, detail-oriented services that bring out the best in your car. With our expert techniques and dedicated approach, we ensure that your car receives the utmost care and attention. Experience a place where passion meets precision and let us create an exceptional car care experience designed just for you.
2. Services:

DETAILING & HAND WASH

• Comprehensive exterior & interior care
• Personalisation and tailored cleaning packages
• Decontamination
• Premium products
• Attention to detail for a perfect finish

POLISHING

• Eliminates scratches, holograms
• Revives and protects paint
• Ensures lasting gloss
• Enhances paint life
• Preserves car’s value and beauty

CERAMIC TREATMENT

• Durable paint protection
• Water-repellent (hydrophobic) effect
• Easier cleaning, enhanced shine
• Long-term surface safeguarding
• Shields against environmental impacts

DRY ICE WASH

• Innovative, waterless method
• Safe for all car parts
• Deep cleans, removes odors
• Allergen-free, antibacterial
• Gentle, effective
• Advanced cleaning technology

COVERING

• Personalized vehicle styling
• More than 150 colours available
• Clean cut without using a cutter
• High-quality, durable materials
• Custom designs available

PROTECTION FILM

• Invisible, durable shield
• Self-healing technology
• 10-year warranty by RQ FOLV

DETAILING BOUTIQUE

• Premium brands available
• Buy on site during your visit
• Granite Assembly, Pip Autos, DRAV Norra
• Essential for at-home car care
• Perfect for quick touch-ups
(for these three brands you can put their logos

Target Market(s)

Our target market includes car owners of all price ranges, with a special focus on those who are passionate about their vehicles. We cater to clients who value excellent service and results, and seek to maintain their cars in pristine condition.

Industry/Entity Type

Automobile / Car detailing

Colors

Designer to choose colors to be used in the design.

Requirements
Must have
• Brand Consistency: The brochure must adhere to our brand colors and style, particularly utilizing the colors present in our logo. Trifold Layout: The design must be specifically tailored for a trifold brochure format. Legibility: Text must be easy to read against the mostly black background, with appropriate font size and style. Professional Look and Feel: The overall design must convey professionalism while being engaging and not overly complex. Photo representation: each service description should have a phot presenting it.
Should not have
• Overcrowded Design: Avoid cluttering with too much text or too many images. The layout should be clean and easy to navigate. Cartoonish Fonts or Graphics: Avoid using unprofessional or casual fonts and graphics that do not align with the upscale and professional image of our business. Distracting Backgrounds: The background should complement and not overpower the content. Stick to the theme of mostly black with design elements from our logo.

```html
<!DOCTYPE html>
<html lang="en">
<head>
<meta charset="utf-8">
<title>Velvet Arc Car Detailing – Trifold Brochure</title>
<link href="https://fonts.googleapis.com/css2?family=Michroma&family=Montserrat:wght@400;500;600;700;800&display=swap" rel="stylesheet">
<style>
:root{
  --page:#ececee;
  --ink:#0a070d;
  --white:#f4f2f7;
  --soft:#d9d4e2;
  --magenta:#c93aa6;
  --purple:#6a2488;
  --violet:#3a1450;
  --blue:#2c8fe0;
  --deep-blue:#17507f;
  --photo-steel:#4d5563;
  --photo-dark:#22262e;
  --photo-orange:#d98a2b;
}
*{margin:0;padding:0;box-sizing:border-box}
html,body{width:1200px;height:900px;overflow:hidden;background:var(--page)}
body{position:relative;font-family:"Montserrat",sans-serif;color:var(--white)}
.spread{position:absolute;top:235px;display:flex;box-shadow:0 18px 30px rgba(0,0,0,.22)}
.spread--outside{left:18px}
.spread--inside{left:618px}
.panel{position:relative;width:188px;height:430px;overflow:hidden;
  background:linear-gradient(175deg,var(--purple) 0%,var(--violet) 14%,var(--ink) 32%,var(--ink) 100%)}
.panel--plain{background:var(--ink)}
.brand-bar{display:flex;align-items:center;gap:6px;padding:18px 12px 0}
.brand-dot{width:18px;height:18px;border-radius:50%;border:1.5px solid var(--magenta);flex:none}
.brand-name{font-size:11.5px;font-weight:400;letter-spacing:.4px;text-transform:uppercase}
.tab{display:inline-block;margin:0 0 4px 10px;padding:2px 30px 2px 6px;font-size:8px;font-weight:800;
  text-transform:uppercase;letter-spacing:.3px;
  background:linear-gradient(90deg,var(--blue),var(--magenta) 70%,transparent);
  clip-path:polygon(4px 0,100% 0,calc(100% - 4px) 100%,0 100%)}
.section{margin-top:14px}
.bullets{list-style:none;padding:0 12px 0 12px;font-size:6.3px;line-height:1.42;color:var(--soft)}
.bullets li::before{content:"· "}
.bullets .note{font-size:6px}
.bullets .note::before{content:""}
.about{padding:0 12px;font-size:6.4px;line-height:1.75;color:var(--soft);text-align:justify}
.photo{position:absolute;left:0;width:100%}
.photo-band{position:absolute;left:0;width:100%;background:linear-gradient(90deg,var(--deep-blue),var(--blue))}
.photo--about{bottom:0;height:190px;clip-path:polygon(0 14%,100% 0,100% 100%,0 100%);
  background:linear-gradient(150deg,var(--photo-steel),var(--photo-dark) 60%,#12151b)}
.band--about{bottom:185px;height:16px;clip-path:polygon(0 80%,100% 0,100% 30%,0 100%)}
/* back panel */
.back{text-align:center;padding-top:22px}
.back-mark{width:62px;height:62px;border-radius:50%;border:2.5px solid var(--magenta);margin:0 auto}
.back-name{font-size:13px;font-weight:400;line-height:1.2;margin-top:8px;text-transform:uppercase}
.hours-title{font-size:9px;font-weight:700;margin-top:30px}
.hours{font-size:8.5px;line-height:1.3;margin-top:8px}
.hours + .hours{margin-top:10px}
.contact-title{font-size:7.5px;font-weight:700;margin-top:34px}
.address{font-size:7px;line-height:1.5;margin-top:4px;color:var(--soft)}
.contact-list{list-style:none;text-align:left;margin:12px 0 0 30px;font-size:7.2px;font-weight:600}
.contact-list li{display:flex;align-items:center;gap:6px;margin-bottom:6px}
.icon{width:10px;height:10px;flex:none}
.icon-square{width:9px;height:9px;background:var(--magenta);border-radius:2px;flex:none}
/* front panel */
.front-head{display:flex;justify-content:space-between;padding:14px 10px 0 12px}
.front-title{font-family:"Michroma",sans-serif;font-size:16px;line-height:1.15;font-weight:400;letter-spacing:.5px}
.front-dot{width:24px;height:24px;border-radius:50%;border:2px solid var(--magenta);margin-top:2px}
.service-list{list-style:none;padding:8px 12px 0 12px;font-size:5.8px;font-weight:600;line-height:1.55;text-transform:uppercase}
.service-list li::before{content:"";display:inline-block;width:4px;height:4px;border-radius:50%;background:var(--magenta);margin-right:6px;vertical-align:middle}
.photo--front{top:140px;height:200px;clip-path:polygon(0 0,100% 22%,100% 100%,0 82%);
  background:linear-gradient(160deg,#7b8290,var(--photo-steel) 40%,var(--photo-dark))}
.band--front{top:328px;height:22px;clip-path:polygon(0 0,100% 40%,100% 100%,0 60%)}
.front-foot{position:absolute;bottom:0;left:0;width:100%;height:92px;text-align:center;padding-top:50px;
  background:linear-gradient(180deg,transparent,var(--violet) 50%,var(--purple))}
.contact-label{font-size:5.8px;font-weight:700;text-transform:uppercase}
.phone-pill{display:inline-block;margin-top:3px;padding:1px 9px;border:1.3px solid var(--white);border-radius:9px;font-size:11px;font-weight:600;letter-spacing:.4px}
/* inside */
.photo--wash{bottom:0;height:158px;clip-path:polygon(0 0,38% 10%,100% 0,100% 100%,0 100%);
  background:linear-gradient(135deg,#5b6470,#2b2f37 45%,#8b93a3 70%,#3a3f48)}
.band--wash{bottom:150px;height:18px;clip-path:polygon(0 0,38% 55%,100% 0,100% 40%,38% 100%,0 40%)}
.photo--dryice{top:0;height:165px;clip-path:polygon(0 0,100% 0,100% 78%,50% 100%,0 78%);
  background:linear-gradient(120deg,#d9dde3,#9aa3ad 35%,#2a4f78 60%,#1d2128)}
.band--dryice{top:130px;height:48px;clip-path:polygon(0 42%,50% 95%,100% 42%,100% 62%,50% 100%,0 62%)}
.middle-text{position:absolute;top:185px;left:0;width:100%}
.middle-text .section{margin-top:9px}
.photo--boutique{bottom:0;height:165px;clip-path:polygon(0 8%,50% 0,100% 8%,100% 100%,0 100%);
  background:radial-gradient(ellipse at 50% 62%,var(--photo-orange) 0 28%,#3a3d44 45%,#1b1d22)}
.band--boutique{bottom:156px;height:20px;clip-path:polygon(0 40%,50% 0,100% 40%,100% 70%,50% 30%,0 70%)}
.fade-top{position:absolute;left:0;width:100%;height:40px;background:linear-gradient(180deg,transparent,var(--violet))}
</style>
</head>
<body>

<!-- Outside spread -->
<section class="spread spread--outside" aria-label="Brochure outside">
  <article class="panel panel--about">
    <header class="brand-bar"><span class="brand-dot"></span><span class="brand-name">Velvet Arc</span></header>
    <div class="section" style="margin-top:22px">
      <span class="tab">About Us</span>
      <p class="about">The ultimate destination for car care in Geneva. We provide personalized, detail oriented services that bring out the best in your car. With our expert techniques and dedicated approach, we ensure that your car receives the utmost care and attention. Experience a place where passion meets precision and let us create an exceptional car care experience designed just for you.</p>
    </div>
    <div class="photo-band band--about"></div>
    <div class="photo photo--about" role="img" aria-label="Photo of a gloved hand polishing a grey car front with a yellow machine pad"></div>
  </article>

  <article class="panel panel--plain back">
    <div class="back-mark"></div>
    <h2 class="back-name">Velvet Arc</h2>
    <p class="hours-title">Opening Hours</p>
    <p class="hours">MON - FRI<br>X.XXam - X.XXpm</p>
    <p class="hours">SAT - SUN<br>X.XXam - X.XXpm</p>
    <p class="contact-title">Contact Us:</p>
    <p class="address">Your addres here, city here<br>street name, zip code 0000</p>
    <ul class="contact-list">
      <li><svg class="icon" viewBox="0 0 10 10"><rect x=".5" y="2" width="9" height="6.5" fill="none" stroke="#c93aa6"/><path d="M.5 2 5 6 9.5 2" fill="none" stroke="#c93aa6"/></svg>hello@velvetarc.ch</li>
      <li><svg class="icon" viewBox="0 0 10 10" fill="none" stroke="#c93aa6" stroke-width=".8"><circle cx="5" cy="5" r="4.3"/><ellipse cx="5" cy="5" rx="2" ry="4.3"/><path d="M.7 5h8.6"/></svg>Your web address here</li>
      <li><span class="icon-square"></span>Your instagram here</li>
      <li><svg class="icon" viewBox="0 0 10 10"><path d="M2 .8 3.8 2.9 2.9 4c.6 1.3 1.7 2.4 3 3l1.1-.9L9.2 8 8 9.4C4.3 9 1 5.7.6 2z" fill="#c93aa6"/></svg>+41 70 555 12 34</li>
    </ul>
  </article>

  <article class="panel panel--front">
    <header class="front-head"><h1 class="front-title">VELVET<br>ARC</h1><span class="front-dot"></span></header>
    <ul class="service-list">
      <li>Detailing &amp; Hand Wash</li><li>Detailing Boutique</li><li>Ceramic Treatment</li>
      <li>Protection Film</li><li>Dry Ice Wash</li><li>Polishing</li><li>Covering</li>
    </ul>
    <div class="photo photo--front" role="img" aria-label="Photo of a hand using an orange rotary polisher on a dark car bonnet"></div>
    <div class="photo-band band--front"></div>
    <footer class="front-foot"><p class="contact-label">Contact us:</p><p class="phone-pill">+41 70 555 12 34</p></footer>
  </article>
</section>

<!-- Inside spread -->
<section class="spread spread--inside" aria-label="Brochure inside">
  <article class="panel">
    <header class="brand-bar"><span class="brand-dot"></span><span class="brand-name">Velvet Arc</span></header>
    <div class="section" style="margin-top:22px">
      <span class="tab">Detailing &amp; Hand Wash</span>
      <ul class="bullets"><li>Comprehensive exterior &amp; interior care</li><li>Personalisation and tailored cleaning packages</li><li>Decontamination</li><li>Premium products</li><li>Attention to detail for a perfect finish</li></ul>
    </div>
    <div class="section">
      <span class="tab">Polishing</span>
      <ul class="bullets"><li>Eliminates scratches, holograms</li><li>Revives and protects paint</li><li>Ensures lasting gloss</li><li>Enhances paint life</li><li>Preserves car’s value and beauty</li></ul>
    </div>
    <div class="photo-band band--wash"></div>
    <div class="photo photo--wash" role="img" aria-label="Photo collage of foam hand washing, a wash mitt and interior machine polishing"></div>
  </article>

  <article class="panel panel--plain">
    <div class="photo photo--dryice" role="img" aria-label="Photo collage of a dry ice cleaning machine releasing vapour and a blue polishing pad"></div>
    <div class="photo-band band--dryice"></div>
    <div class="middle-text">
      <div class="section"><span class="tab">Ceramic Treatment</span>
        <ul class="bullets"><li>Durable paint protection</li><li>Water-repellent (hydrophobic) effect</li><li>Easier cleaning, enhanced shine</li><li>Long-term surface safeguarding</li><li>Shields against environmental impacts</li></ul></div>
      <div class="section"><span class="tab">Dry Ice Wash</span>
        <ul class="bullets"><li>Innovative, waterless method</li><li>Safe for all car parts</li><li>Deep cleans, removes odors</li><li>Allergen-free, antibacterial</li><li>Gentle, effective</li></ul></div>
      <div class="section"><span class="tab">Covering</span>
        <ul class="bullets"><li>Personalized vehicle styling</li><li>More than 150 colours available</li><li>Clean cut without using a cutter</li><li>High-quality, durable materials</li><li>Custom designs available</li></ul></div>
    </div>
  </article>

  <article class="panel">
    <header class="brand-bar"><span class="brand-dot"></span><span class="brand-name">Velvet Arc</span></header>
    <div class="section" style="margin-top:22px">
      <span class="tab">Protection Film</span>
      <ul class="bullets"><li>Invisible, durable shield</li><li>Self-healing technology</li><li>10-year warranty by RQ FOLV</li></ul>
    </div>
    <div class="section">
      <span class="tab">Detailing Boutique</span>
      <ul class="bullets"><li>Premium brands available</li><li>Buy on site during your visit</li><li>Granite Assembly, Pip Autos, DRAV Norra</li><li>Essential for at-home car care</li><li>Perfect for quick touch-ups</li><li class="note">(for these three brands you can put their logos)</li></ul>
    </div>
    <div class="photo-band band--boutique"></div>
    <div class="photo photo--boutique" role="img" aria-label="Photo of detailing products, an orange microfibre towel and a black applicator on carbon fibre"></div>
  </article>
</section>

</body>
</html>
```